Vintage "Greetings from Door County" Design for Wall

I are looking to recreate the vintage "Greetings from" postcard graphic from the 1940-50s. The main focus will be the saying "Greetings from Door County". Door County is a resort area in Wisconsin and we will use this graphic as a backdrop for tourist's instagram pictures. The letters of "Door County" will include things that the area is known for such as swimming, fishing, beaches, boating, biking, camping, cherry orchards, sunsets on the water etc. I have attached an actual postcard from the 50s for Door County to help you visualize the project (Picture 1). I have also attached landmarks and iconic features of Door County to include in the letters (Pictures 2-10). I want it to be more whimsical in nature with drawings to depict these landmarks as opposed to actual realistic pictures (Example 1 & 2). Please ask any questions to help clarify the project. Thanks and good luck!
Target Market(s)
Tourists
Industry/Entity Type
Retail
Colors
Designer to choose colors to be used in the design.
Look and feel

```html
<!DOCTYPE html>
<html lang="en">
<head>
<meta charset="utf-8">
<title>Greetings from Door County</title>
<link rel="stylesheet" href="https://fonts.googleapis.com/css2?family=Bowlby+One&family=Yellowtail&display=swap">
<style>
  :root {
    --sky-top: #2e4660;
    --sky-mid: #8a8a6e;
    --horizon: #f08a1c;
    --sun: #ffd24a;
    --water-top: #8a5a24;
    --water-deep: #2a2218;
    --letter-edge: #c9561a;
    --letter-shadow: #1a1208;
    --gold-light: #f3dc96;
    --gold-dark: #8a5e1c;
    --script-edge: #5a3a10;
  }
  html, body {
    margin: 0;
    padding: 0;
    width: 1200px;
    height: 931px;
    overflow: hidden;
    background: #ffffff;
  }
  .postcard {
    display: block;
    width: 1200px;
    height: 931px;
  }
  .greeting {
    font-family: "Yellowtail", "Brush Script MT", cursive;
    font-size: 100px;
  }
  .big-word {
    font-family: "Bowlby One", "Arial Black", sans-serif;
  }
  .word-door { font-size: 550px; }
  .word-county { font-size: 380px; }
</style>
</head>
<body>
<svg class="postcard" viewBox="0 0 1200 931" xmlns="http://www.w3.org/2000/svg">
  <defs>
    <linearGradient id="scene-sky" x1="0" y1="0" x2="0" y2="1">
      <stop offset="0" stop-color="var(--sky-top)"/>
      <stop offset="0.25" stop-color="var(--sky-mid)"/>
      <stop offset="0.45" stop-color="var(--horizon)"/>
      <stop offset="0.5" stop-color="var(--sun)"/>
      <stop offset="0.56" stop-color="var(--water-top)"/>
      <stop offset="1" stop-color="var(--water-deep)"/>
    </linearGradient>
    <linearGradient id="door-fill" x1="0" y1="0" x2="1" y2="0">
      <stop offset="0" stop-color="#7a9a4a"/>
      <stop offset="0.25" stop-color="#4e6a2a"/>
      <stop offset="0.45" stop-color="#8a7a3a"/>
      <stop offset="0.6" stop-color="#e8e8e2"/>
      <stop offset="0.8" stop-color="#cfd6cf"/>
      <stop offset="1" stop-color="#9eb4b0"/>
    </linearGradient>
    <linearGradient id="county-fill" x1="0" y1="0" x2="1" y2="0">
      <stop offset="0" stop-color="#5a8a7a"/>
      <stop offset="0.25" stop-color="#e6e2d6"/>
      <stop offset="0.42" stop-color="#d4641e"/>
      <stop offset="0.6" stop-color="#b8301a"/>
      <stop offset="0.75" stop-color="#6aa0b8"/>
      <stop offset="1" stop-color="#8a5a3a"/>
    </linearGradient>
    <linearGradient id="gold" x1="0" y1="0" x2="0" y2="1">
      <stop offset="0" stop-color="var(--gold-light)"/>
      <stop offset="0.55" stop-color="#c99a44"/>
      <stop offset="1" stop-color="var(--gold-dark)"/>
    </linearGradient>
  </defs>

  <rect class="scene-backdrop" x="0" y="0" width="1200" height="931" fill="url(#scene-sky)"
        role="img" aria-label="Sunset over the bay with clouds and rippling water"/>

  <g class="headline-block" role="img" aria-label="Letters filled with scenes of bluffs, a ferry, a lighthouse, autumn trees, a lookout tower and a barn">
    <text class="big-word word-door" x="96" y="564" textLength="1030" lengthAdjust="spacingAndGlyphs"
          fill="var(--letter-shadow)" opacity="0.85">DOOR</text>
    <text class="big-word word-door" x="82" y="550" textLength="1030" lengthAdjust="spacingAndGlyphs"
          fill="url(#door-fill)" stroke="var(--letter-edge)" stroke-width="7">DOOR</text>

    <text class="big-word word-county" x="100" y="836" textLength="1030" lengthAdjust="spacingAndGlyphs"
          fill="var(--letter-shadow)" opacity="0.85">COUNTY</text>
    <text class="big-word word-county" x="86" y="822" textLength="1030" lengthAdjust="spacingAndGlyphs"
          fill="url(#county-fill)" stroke="var(--letter-edge)" stroke-width="7">COUNTY</text>
  </g>

  <g class="headline-script">
    <text class="greeting" x="83" y="158" textLength="620" lengthAdjust="spacingAndGlyphs"
          fill="var(--letter-shadow)" opacity="0.75">Greetings from</text>
    <text class="greeting" x="78" y="152" textLength="620" lengthAdjust="spacingAndGlyphs"
          fill="url(#gold)" stroke="var(--script-edge)" stroke-width="1.5">Greetings from</text>
  </g>
</svg>
</body>
</html>
```